Cask Annals, a definitive reference book on port

My husband has just finished writing a big book on Vintage Port. We need a hardcover book flap design for this book that is impressively huge. It's taken 10 years to research and write. It's 650 pages, interior is A4, exterior 4mm larger, and weighs nearly 3 kilos. It's a special book for people in the wine and port industry, as well as for someone who loves to drink Vintage Port. It can be a beautiful coffeetable book too.

The book is mainly about port and its declared vintages. It's also about the history of port, who drank it, when, how, where, who bought it, for how much, and the port houses are also described in detail.

The wine expert Tobias Quellmore wrote a book about vintage wine in 2002, and my husband would like to have a similar cover for his book. (A photo attached in files). I've attached other photos to give the designers an idea of the look and feel of the 'port culture', as well as photos of the typeface that my husband will be using for the inside hardcover.

Target Market(s)

Wine and port industry. Wine aficionados.

Industry/Entity Type

Winery

Font styles to use
Sans Serif
Script

Colors
ec1f27
1b1b1b
474747
333333
5c5c5c
faa54b

Requirements
Must have
• Book Cover must have Title: "Cask Annals" and "R. K. P. Holloway" (files attached to show proper typeface). One of the files is a flap jacket book cover that my husband designed himself. We're looking for more design ideas, and that pdf is a close winner to what he wants.
Nice to have
• illustration or painting of port glasses, or grapes, or similar. Dark colors, especially port wine, deep red wine colors. Gold writing, black writing, with red/berry/maroon accents. Luxury, elegance, has a masculine edge, traditional, but not too old-school and boring (like grandpa). Textures that are including with the culture of drinking vintage port are leather, velvet, cigar, wood, marble, winter, fireplaces. This sounds quite heavy, but it also should be simple and clean. I hope this isn't too confusing. Thanks!
Should not have
• Bright colors, playfulness.

```html
<!DOCTYPE html>
<html lang="en">
<head>
<meta charset="utf-8">
<title>Cask Annals — Cover</title>
<link rel="stylesheet" href="https://fonts.googleapis.com/css2?family=EB+Garamond:wght@400;500&display=swap">
<style>
  :root {
    --page-bg: #ffffff;
    --cover-deep: #4e1214;
    --cover-mid: #5e1c1f;
    --cover-light: #6a2628;
    --ink-cream: #e6dcc2;
    --art-tone: #6e2e2b;
    --art-tone-light: #7e3c37;
  }
  * { box-sizing: border-box; margin: 0; padding: 0; }
  html, body {
    width: 1200px;
    height: 1106px;
    overflow: hidden;
    background: var(--page-bg);
  }
  .canvas {
    position: relative;
    width: 1200px;
    height: 1106px;
  }
  .cover {
    position: absolute;
    left: 250px;
    top: 58px;
    width: 700px;
    height: 990px;
    background:
      radial-gradient(ellipse at 70% 30%, var(--cover-light) 0%, transparent 60%),
      linear-gradient(160deg, var(--cover-mid) 0%, var(--cover-deep) 100%);
    color: var(--ink-cream);
    font-family: "EB Garamond", Garamond, serif;
    display: flex;
    flex-direction: column;
    align-items: center;
    text-align: center;
  }
  .cover-title {
    margin-top: 72px;
    font-weight: 400;
    font-size: 138px;
    line-height: 1.02;
    letter-spacing: 1px;
    text-transform: uppercase;
  }
  .cover-title span { display: block; }
  .cover-subtitle {
    margin-top: 34px;
    font-size: 39px;
    line-height: 1.22;
    font-weight: 400;
  }
  .cover-art {
    margin-top: 54px;
    width: 230px;
    height: 290px;
    border-radius: 8px;
    background: radial-gradient(ellipse at 50% 55%, var(--art-tone-light) 0%, var(--art-tone) 55%, transparent 80%);
    opacity: 0.8;
  }
  .cover-author {
    margin-top: auto;
    margin-bottom: 100px;
    font-size: 40px;
    font-weight: 500;
    letter-spacing: 1px;
    text-transform: uppercase;
  }
</style>
</head>
<body>
  <main class="canvas">
    <section class="cover">
      <h1 class="cover-title"><span>Cask</span><span>Annals</span></h1>
      <p class="cover-subtitle">The Record of Declared Ports,<br>Across the Centuries,<br>Documented and Thorough in Full</p>
      <div class="cover-art" role="img" aria-label="Line sketch of a port bottle, a filled wine glass and a bunch of grapes with leaves"></div>
      <p class="cover-author">R. K. P. Holloway</p>
    </section>
  </main>
</body>
</html>
```